Pediatric Vision Care: Myopia Control Brochure

We are a pediatric eye care practice (ophthalmology and optometry). One of our services we offer for children is myopia control, which are strategies for slowing or stopping the progression of nearsightedness. This is a service we need to sell to parents because most insurance won't pay for it. There are different options we offer that can work well for kids in different situations: glasses with Corvane lenses, atropine eye drops, and/or special contact lenses. We need a brochure we can distribute to parents to let them know about this service that would encourage them to buy it for children who need it. Attached is our initial draft brochure created by our staff that provides text that we want to keep. The images and layout can change. We probably need at least one or two photos of kids on the brochure, because this is only something that works for children who are still growing, and the target audience is parents of 4-8 year old children.

Target Market(s)

Parents of 4-8 year old children

Font styles to use
Sans Serif

Requirements
Must have
• I'm uploading our company logo that should be included somewhere on the brochure. You can include contact information (web address, phone number) for our practice that is found on our website: http://www.brookhollowkidsvision.com/
Should not have
• This should not look childish. We need the impression to be friendly but professional, medical, expert.

```html
<!DOCTYPE html>
<html lang="en">
<head>
<meta charset="utf-8">
<title>Myopia Control – Treatment and Environmental Options</title>
<link rel="stylesheet" href="https://fonts.googleapis.com/css2?family=Montserrat:wght@400;500;700&display=swap">
<style>
  :root {
    --leaf: #9fd800;
    --leaf-bg: #f1f7d9;
    --peach-bg: #fdeedd;
    --orange: #ff8a00;
    --ink: #1c1c1c;
    --text: #2b2b2b;
  }
  * { box-sizing: border-box; margin: 0; padding: 0; }
  html, body { width: 1200px; height: 848px; overflow: hidden; }
  body {
    position: relative;
    font-family: "Montserrat", sans-serif;
    color: var(--text);
    background: var(--leaf-bg);
  }
  .panel-environment {
    position: absolute; left: 800px; top: 0; width: 400px; height: 848px;
    background: var(--peach-bg);
  }
  .rule { position: absolute; top: 50px; height: 8px; }
  .rule--green { left: 50px; width: 750px; background: var(--leaf); }
  .rule--orange { left: 800px; width: 349px; background: var(--orange); }

  .section-title {
    position: absolute; top: 92px;
    font-size: 22px; font-weight: 700; color: var(--ink); letter-spacing: 0.6px;
  }
  .section-title--treatment { left: 49px; }
  .section-title--environment { left: 851px; }

  .pill {
    position: absolute; height: 33px; padding: 0 16px 0 11px;
    background: var(--leaf); color: #fff;
    font-size: 16px; font-weight: 700; letter-spacing: 0.5px;
    line-height: 33px; border-radius: 0 17px 17px 0;
  }

  .copy {
    position: absolute;
    font-size: 13.3px; line-height: 20px; letter-spacing: 0.35px; font-weight: 400;
  }
  .copy p + p { margin-top: 18.8px; }
  .copy--env { line-height: 18.8px; }

  .photo { display: block; }
  .photo--float { float: right; }

  .photo--lens { width: 168px; height: 150px; margin: -1px 0 0 8px;
    background: radial-gradient(circle at 50% 50%, #c9f0f5 0%, #7cd2e0 45%, #3a8fb5 100%); }
  .photo--drops { float: left; width: 168px; height: 150px; margin: 2px 12px 0 0;
    background: linear-gradient(160deg, #e8ecf7 0%, #c6d0ee 55%, #9fb0dd 100%); }
  .photo--contact { width: 168px; height: 150px; margin: 2px 0 0 10px;
    background: linear-gradient(140deg, #dcecf6 0%, #bfd9ea 50%, #e8b49a 100%); }

  .photo--exam {
    position: absolute; left: 426px; top: 120px; width: 374px; height: 355px;
    background: linear-gradient(110deg, #6b4a3a 0%, #e9e9ec 35%, #f4f4f4 60%, #c9b9aa 100%);
  }
  .photo--park {
    position: absolute; left: 800px; top: 557px; width: 400px; height: 291px;
    background: linear-gradient(180deg, #e8eef2 0%, #8fae5c 40%, #6f9a3a 70%, #a3c25a 100%);
  }
  .highlight { color: var(--orange); font-weight: 700; }
</style>
</head>
<body>
  <div class="panel-environment"></div>
  <div class="rule rule--green"></div>
  <div class="rule rule--orange"></div>

  <h1 class="section-title section-title--treatment">Several treatment options</h1>
  <h1 class="section-title section-title--environment">Environmental options</h1>

  <!-- Glasses lenses -->
  <div class="pill" style="left:50px; top:146px;">Lumora Corvane glasses lenses</div>
  <div class="copy" style="left:51px; top:194px; width:325px;">
    <div class="photo photo--float photo--lens" role="img" aria-label="Close-up of a myopia control spectacle lens with concentric micro-lenslet rings"></div>
    <p>FDA market authorized Lumora Corvane glasses lenses have been shown to slow myopia progression by about 50% in children aged 6-12. These lenses are a great treatment option because all your child needs to do is wear glasses. They look almost identical to ordinary glasses, but use specialized optics to signal the brain to slow the growth of myopic eyes.</p>
  </div>

  <div class="photo photo--exam" role="img" aria-label="Eye doctor examining a smiling young girl at a slit lamp, eye chart in the background"></div>

  <!-- Atropine -->
  <div class="pill" style="left:50px; top:506px;">Low-dose atropine</div>
  <div class="copy" style="left:51px; top:555px; width:325px;">
    <div class="photo photo--drops" role="img" aria-label="Dropper bottle releasing a single eye drop"></div>
    <p>These eyedrops have been studied for over 20 years and have been shown to slow myopia progression by about 50% when used consistently. Low-dose atropine is simple to add to your daily routine. One drop is placed in each eye before bed each evening. These are ordered from a compounding pharmacy and mailed directly to your home.</p>
  </div>

  <!-- Contact lenses -->
  <div class="pill" style="left:426px; top:506px;">Specialty contact lenses</div>
  <div class="copy" style="left:426px; top:555px; width:326px;">
    <div class="photo photo--float photo--contact" role="img" aria-label="Soft contact lens balanced on a fingertip next to a lens case"></div>
    <p>FDA-approved Veridia lenses have been shown to slow myopia progression by about 50% in children aged 8-12. Contact lenses can be a great fit for many children, especially active children or those who do not enjoy wearing glasses. Many children as young as 7 or 8 are successful at wearing contacts.</p>
  </div>

  <!-- Environmental -->
  <div class="copy copy--env" style="left:851px; top:146px; width:300px;">
    <p>All myopic children can benefit from these lifestyle changes.</p>
    <p>It is important to get your child <span class="highlight">outdoors</span> consistently. There is strong evidence that children who spend at least <span class="highlight">2 hours a day</span> outdoors are less likely to become myopic, and their myopia progresses slower than children who are outdoors less. Some studies show that increasing outdoor time by as few as 45 minutes a day is beneficial in reducing progression.</p>
    <p>There is some evidence that consistent use of screens, particularly held very close to the face, can worsen nearsightedness. We recommend limiting non- academic screen time and near work, and encourage your child to use the <span class="highlight">20-20-20 rule</span>. Every 20 minutes take a 20 second break to look at least 20 feet away.</p>
  </div>

  <div class="photo photo--park" role="img" aria-label="Four happy children running across a sunny park lawn with trees behind them"></div>
</body>
</html>
```